Property refurbishment & maintenance Business Card Design

Velkoran Ltd is a leading provider of domestic maintenance, building and refurbishment services. Founded in October 2009 by Milo Velkoran, we aim to provide our customers with exceptional home improvement and maintenance services whilst minimising the disruption and stress caused.
The building services we provide are of the very highest quality. We provide all of your customers with the peace of mind in knowing that they are dealing with experts in construction, renovation and decoration. This is because we are members of the Guild of Certified Tradecrafters (GCT). We have also had our credentials verified by Pledgeline and the UK government's Fair Seal scheme.
Target Market(s)
Private home owners,letting agents,tenants
Industry/Entity Type
Home Improvement
Contact Information for Business Card
Velkoran ltd.
Milo Velkoran
18 Brindle Cope Lane ,Waltham Cross,Herts,EN4 2QW,T.01632960517 M:07700900382
E. info@velkoran.co.uk. www.velkoran.co.uk

```html
<!DOCTYPE html>
<html lang="en">
<head>
<meta charset="utf-8">
<title>Velkoran Ltd – Business Card</title>
<link rel="stylesheet" href="https://fonts.googleapis.com/css2?family=Exo+2:wght@400;500;700&display=swap">
<style>
  :root {
    --stage: #1c1c1e;
    --card: #fbfbfb;
    --ink: #2e2e30;
    --ink-soft: #555659;
    --brand-blue: #2a6fd6;
    --brand-blue-deep: #1b4fb8;
    --brand-blue-light: #3c94e6;
    --strip-grey: #3a3b3e;
    --white: #ffffff;
  }
  * { box-sizing: border-box; margin: 0; padding: 0; }
  html, body {
    width: 1200px; height: 862px; overflow: hidden;
    background: var(--stage);
    font-family: "Exo 2", "Helvetica Neue", Arial, sans-serif;
  }
  .canvas {
    position: relative; width: 1200px; height: 862px;
    display: flex; justify-content: center; align-items: center; gap: 60px;
  }
  .card {
    position: relative; width: 380px; height: 665px;
    background: var(--card);
    overflow: hidden;
  }

  /* front */
  .card-front .top-strip {
    position: absolute; top: 0; left: 0; width: 100%; height: 34px;
  }
  .brand {
    position: absolute; left: 0; right: 0;
    display: flex; align-items: center; justify-content: center; gap: 12px;
  }
  .brand-mark {
    width: 22px; height: 22px; background: var(--brand-blue);
  }
  .brand-name {
    font-size: 34px; font-weight: 400; color: var(--ink); letter-spacing: 0.5px;
  }
  .card-front .brand { top: 150px; }
  .person { position: absolute; left: 70px; top: 262px; }
  .person-name {
    font-size: 33px; font-weight: 700; color: var(--ink); letter-spacing: 1px; line-height: 1;
  }
  .person-title {
    margin-top: 6px; font-size: 15px; font-weight: 500; color: var(--brand-blue);
    letter-spacing: 1.6px; text-transform: uppercase;
  }
  .contact-row {
    position: absolute; left: 70px; display: flex; align-items: center; gap: 14px;
  }
  .contact-row svg { width: 30px; height: 30px; flex: none; }
  .contact-lines { font-size: 15px; color: var(--ink-soft); line-height: 1.45; letter-spacing: 0.6px; }
  .contact-phone { top: 362px; }
  .contact-web { top: 430px; }
  .address-band {
    position: absolute; left: 0; bottom: 0; width: 100%; height: 150px;
  }
  .address-band svg { position: absolute; inset: 0; width: 100%; height: 100%; }
  .address-text {
    position: absolute; left: 0; right: 0; top: 58px; text-align: center;
    color: var(--white); font-size: 19px; line-height: 1.45; letter-spacing: 0.6px;
  }

  /* back */
  .card-back .brand { top: 250px; }
  .card-back .brand-name { font-size: 38px; }
  .card-back .brand-mark { width: 26px; height: 26px; }
  .back-web {
    position: absolute; left: 0; right: 0; bottom: 40px; text-align: center;
    font-size: 15px; color: var(--ink); letter-spacing: 1px;
  }
</style>
</head>
<body>
<main class="canvas">

  <section class="card card-front" aria-label="Business card front">
    <svg class="top-strip" viewBox="0 0 380 34" preserveAspectRatio="none" aria-hidden="true">
      <path d="M0 0 H380 V10 Q380 20 366 20 H14 Q0 20 0 34 Z" fill="var(--strip-grey)"/>
    </svg>

    <div class="brand">
      <span class="brand-mark"></span>
      <span class="brand-name">Velkoran Ltd</span>
    </div>

    <div class="person">
      <p class="person-name">JONAH PELL</p>
      <p class="person-title">General Manager</p>
    </div>

    <div class="contact-row contact-phone">
      <svg viewBox="0 0 30 30" aria-hidden="true">
        <circle cx="15" cy="15" r="13.5" fill="none" stroke="var(--ink)" stroke-width="1.6"/>
        <path d="M9.5 10.5 Q9 8.5 11 8 L12.6 10.6 L11.4 12 Q12.6 15.6 16.8 17.4 L18.2 16.2 L21 17.8 Q20.6 20 18.4 19.8 Q11 18.4 9.5 10.5 Z" fill="var(--ink)"/>
      </svg>
      <div class="contact-lines">
        <p>01632 960 517</p>
        <p>07700 900 382</p>
      </div>
    </div>

    <div class="contact-row contact-web">
      <svg viewBox="0 0 30 30" aria-hidden="true">
        <circle cx="15" cy="15" r="13.5" fill="none" stroke="var(--ink)" stroke-width="1.6"/>
        <circle cx="15" cy="15" r="8" fill="none" stroke="var(--ink)" stroke-width="1.4"/>
        <ellipse cx="15" cy="15" rx="3.6" ry="8" fill="none" stroke="var(--ink)" stroke-width="1.2"/>
        <path d="M7 15 H23 M8.2 11 H21.8 M8.2 19 H21.8" stroke="var(--ink)" stroke-width="1.1"/>
      </svg>
      <div class="contact-lines">
        <p>name@velkoran.co.uk</p>
        <p>www.velkoran.co.uk</p>
      </div>
    </div>

    <div class="address-band">
      <svg viewBox="0 0 380 150" preserveAspectRatio="none" aria-hidden="true">
        <defs>
          <linearGradient id="bandFill" x1="0" y1="0" x2="1" y2="0">
            <stop offset="0" stop-color="var(--brand-blue-deep)"/>
            <stop offset="0.6" stop-color="var(--brand-blue)"/>
            <stop offset="1" stop-color="var(--brand-blue-light)"/>
          </linearGradient>
        </defs>
        <path d="M0 150 V42 Q0 24 22 28 Q60 36 70 36 H300 Q340 36 356 16 Q368 0 380 0 V150 Z" fill="url(#bandFill)"/>
      </svg>
      <p class="address-text">18 Brindle Cope Lane,<br>Waltham Cross</p>
    </div>
  </section>

  <section class="card card-back" aria-label="Business card back">
    <div class="brand">
      <span class="brand-mark"></span>
      <span class="brand-name">Velkoran Ltd</span>
    </div>
    <p class="back-web">www.velkoran.co.uk</p>
  </section>

</main>
</body>
</html>
```